Company or website name
- LORAVEX
- Links to the website
- WWW.LORAVEX.NET
- Describe your company and organization and target audience
- check the website: www.loravex.net
- The design should have the following
- A clean visual is expected. The documents should include the complete address, emails, phone, name and position.
- Other Facts

```html
<!DOCTYPE html>
<html lang="en">
<head>
<meta charset="utf-8">
<title>LORAVEX Business Cards</title>
<link rel="stylesheet" href="https://fonts.googleapis.com/css2?family=Montserrat:wght@400;500&family=Open+Sans:wght@400;600;700&display=swap">
<style>
  :root {
    --bg: #ebe8e5;
    --navy: #0e3457;
    --teal: #5cc3d4;
    --paper: #f1f1f0;
    --white: #ffffff;
    --soft: #d9e3ec;
  }
  * { box-sizing: border-box; margin: 0; padding: 0; }
  html, body { width: 1200px; height: 944px; overflow: hidden; }
  body { background: var(--bg); position: relative; font-family: "Open Sans", sans-serif; }

  .card {
    position: absolute;
    width: 520px;
    height: 297px;
    box-shadow: 0 2px 6px rgba(0,0,0,0.12);
    overflow: hidden;
  }

  /* Front face */
  .card-front {
    left: 90px; top: 150px;
    background: var(--navy);
  }
  .card-front .company {
    position: absolute;
    left: 0; right: 0; top: 128px;
    text-align: center;
    font-family: "Montserrat", sans-serif;
    font-weight: 500;
    font-size: 25px;
    letter-spacing: 1px;
    color: var(--white);
  }
  .card-front .company .tagline { color: var(--teal); }
  .card-front .website {
    position: absolute;
    left: 0; right: 0; top: 236px;
    text-align: center;
    font-family: "Montserrat", sans-serif;
    font-size: 11px;
    letter-spacing: 4px;
    color: var(--soft);
  }

  /* Back face */
  .card-back {
    left: 590px; top: 497px;
    background: var(--paper);
    display: flex;
  }
  .brand-side {
    width: 248px;
    height: 100%;
    display: flex;
    align-items: center;
    justify-content: center;
  }
  .brand-name {
    font-family: "Montserrat", sans-serif;
    font-weight: 400;
    font-size: 44px;
    letter-spacing: 1px;
    color: var(--navy);
  }
  .divider { width: 6px; height: 100%; background: var(--teal); }
  .info-side {
    flex: 1;
    background: var(--navy);
    padding: 40px 0 0 26px;
    color: var(--soft);
  }
  .person-name {
    font-weight: 700;
    font-size: 20px;
    color: var(--white);
    line-height: 1.1;
  }
  .person-role {
    font-size: 12px;
    color: var(--teal);
    margin-bottom: 22px;
  }
  .address { font-size: 12px; line-height: 1.35; margin-bottom: 22px; }
  .contacts { list-style: none; font-size: 12px; line-height: 1.4; }
  .contacts li { display: flex; align-items: center; gap: 8px; }
  .contacts svg { width: 12px; height: 12px; flex: none; }
</style>
</head>
<body>

<section class="card card-front">
  <h1 class="company">LORAVEX <span class="tagline">DRILLING SUPPLIES</span></h1>
  <p class="website">www.loravex.net</p>
</section>

<section class="card card-back">
  <div class="brand-side">
    <span class="brand-name">LORAVEX</span>
  </div>
  <div class="divider"></div>
  <div class="info-side">
    <p class="person-name">Dane Holloway</p>
    <p class="person-role">President</p>
    <p class="address">Calle Brisas, Loma Verde<br>Ciudad Norte</p>
    <ul class="contacts">
      <li>
        <svg viewBox="0 0 12 12"><path d="M2.5 1 L4.5 1 L5.3 3.6 L4 4.6 Q5.2 7 7.4 8 L8.4 6.7 L11 7.5 L11 9.5 Q10.5 11 9 11 Q1 10 1 2.5 Q1 1 2.5 1 Z" fill="var(--teal)"/></svg>
        +507 555-0142
      </li>
      <li>
        <svg viewBox="0 0 12 12"><rect x="3" y="0.8" width="6" height="10.4" rx="1" fill="none" stroke="var(--teal)" stroke-width="1.2"/><circle cx="6" cy="9.4" r="0.6" fill="var(--teal)"/></svg>
        +507 6555-0178
      </li>
      <li>
        <svg viewBox="0 0 12 12"><rect x="0.5" y="2.5" width="11" height="7.5" rx="0.8" fill="var(--teal)"/><path d="M0.8 3 L6 7 L11.2 3" fill="none" stroke="var(--navy)" stroke-width="0.9"/></svg>
        sales@loravex.net
      </li>
      <li>
        <svg viewBox="0 0 12 12"><circle cx="6" cy="6" r="5.3" fill="var(--teal)"/><path d="M0.8 6 H11.2 M6 0.7 Q3 6 6 11.3 M6 0.7 Q9 6 6 11.3" fill="none" stroke="var(--navy)" stroke-width="0.8"/></svg>
        www.loravex.net
      </li>
    </ul>
  </div>
</section>

</body>
</html>
```